I have written a book called "Velvet Compass Diaries - Uncover hidden profit tricks insiders quietly bill huge sums over decades, hoping nobody ever finds out"

This book will be sold through this webpage as an ebook. i have attached a copy of the cover of the book and I would like the website to be consistent with the look and feel of the book cover.

Target Market(s)

Business owners

Industry/Entity Type

Business

Requirements
Must have
• There has been a video produced for the promotion of this book which is yet to be completed. The video will be on ClipVaro and the video needs to be prominent on the homepage.

I need to be able to manage and change the content as I wish on the website eg wordpress.

The page will need have a Quidora purchase button

Also a 100% money back guarantee sign

Nice to have
• Chatterly plug in to show how many people like the page

Should not have
• I don't want the homepage or any of the other pages to be too cluttered

```html
<!DOCTYPE html>
<html lang="en">
<head>
<meta charset="utf-8">
<title>Velvet Compass Diaries</title>
<link href="https://fonts.googleapis.com/css2?family=Josefin+Sans:wght@600;700&family=Open+Sans:wght@400;600&display=swap" rel="stylesheet">
<style>
  :root{
    --dark:#232323;
    --darker:#161616;
    --paper:#efefef;
    --blue:#00aaea;
    --white:#ffffff;
    --ink:#1b1b1b;
    --muted:#9a9a9a;
    --card:#e9e9e9;
    --line:#cfcfcf;
  }
  *{box-sizing:border-box;margin:0;padding:0}
  html,body{width:780px;height:1200px;overflow:hidden}
  body{position:relative;background:var(--paper);font-family:"Open Sans",Arial,sans-serif;color:var(--ink)}

  .site-header{position:absolute;left:0;top:0;width:780px;height:118px;background:var(--dark)}
  .site-title{position:absolute;top:28px;width:100%;text-align:center;font-family:"Josefin Sans",sans-serif;font-weight:700;font-size:36px;letter-spacing:1px;color:var(--white);line-height:1}
  .site-title .accent{color:var(--blue)}
  .main-nav{position:absolute;top:91px;width:100%;display:flex;justify-content:center;gap:16px;font-size:10px;text-transform:uppercase}
  .main-nav a{color:var(--white);text-decoration:none}
  .main-nav a.is-current{color:var(--blue)}
  .nav-rule{position:absolute;left:188px;top:115px;width:403px;height:3px;background:var(--blue)}
  .nav-pointer{position:absolute;left:285px;top:109px;width:0;height:0;border-left:6px solid transparent;border-right:6px solid transparent;border-bottom:6px solid var(--blue)}

  .book-cover{position:absolute;left:188px;top:150px;width:403px;height:571px;background:var(--blue);overflow:hidden;box-shadow:0 2px 6px rgba(0,0,0,.25)}
  .cover-card{position:absolute;left:8px;top:80px;width:296px;height:190px;background:linear-gradient(180deg,#f6f6f6,var(--card));transform:rotate(-10deg);transform-origin:left top;padding:40px 16px 0 28px;z-index:2}
  .cover-title{font-weight:600;font-size:32px;line-height:1.05;color:var(--ink)}
  .cover-tagline{margin-top:10px;font-size:10px;line-height:1.35;text-transform:uppercase;color:#555;text-align:center}
  .cover-figure{position:absolute;right:0;top:178px;width:140px;height:393px;background:linear-gradient(180deg,#1a1a1a,#000);border-radius:60px 0 0 0;opacity:.9}
  .cover-author{position:absolute;left:28px;bottom:26px;font-size:18px;color:var(--white)}
  .cover-author .by{color:#4a4a4a}
  .cover-author .cred{font-size:10px}

  .like-widget{position:absolute;left:200px;top:760px;width:80px;display:flex;flex-direction:column;align-items:center;gap:6px}
  .like-count{width:46px;height:24px;background:var(--white);border:1px solid var(--line);font-size:10px;font-weight:600;color:var(--ink);display:flex;align-items:center;justify-content:center}
  .like-brand{display:flex;align-items:center;gap:4px;font-size:11px;font-weight:600;color:var(--ink)}
  .like-brand .square{width:7px;height:7px;background:var(--blue)}

  .guarantee-badge{position:absolute;left:347px;top:741px;width:86px;height:86px}

  .pay-brand{position:absolute;left:500px;top:770px;font-weight:600;font-size:18px;color:#1f3f8f;display:flex;align-items:center;gap:6px}
  .pay-brand .dot{width:10px;height:10px;border-radius:50%;background:#1f3f8f}

  .promo{position:absolute;left:0;top:849px;width:780px;height:327px;background:var(--dark)}
  .promo-rule{position:absolute;left:188px;top:845px;width:403px;height:4px;background:var(--blue)}
  .promo-pointer{position:absolute;left:384px;top:849px;border-left:7px solid transparent;border-right:7px solid transparent;border-top:7px solid var(--blue)}
  .promo-heading{position:absolute;top:880px;width:100%;text-align:center;font-family:"Josefin Sans",sans-serif;font-weight:700;font-size:16px;letter-spacing:1px;color:var(--white)}

  .video-player{position:absolute;left:219px;top:920px;width:342px;height:210px;background:#000;border:2px solid var(--white);z-index:2}
  .video-shadow{position:absolute;left:170px;top:1120px;width:440px;height:22px;border-radius:50%;background:radial-gradient(ellipse at center,rgba(0,0,0,.75),rgba(0,0,0,0) 70%)}
  .video-progress{position:absolute;left:0;bottom:20px;width:100%;height:6px;background:#555}
  .video-controls{position:absolute;left:0;bottom:0;width:100%;height:20px;background:linear-gradient(#f4f4f4,#d8d8d8);display:flex;align-items:center;font-size:7px;color:#333;padding:0 6px;gap:8px}
  .video-controls .time{margin-right:auto;padding-left:4px}
  .video-controls svg{display:block}
  .spinner{position:absolute;left:162px;top:88px}

  .site-footer{position:absolute;left:0;top:1176px;width:780px;height:24px;background:var(--darker);font-size:6.5px;color:var(--muted);text-transform:uppercase;letter-spacing:.3px}
  .site-footer .copyright{position:absolute;left:84px;top:8px}
  .site-footer .legal{position:absolute;right:84px;top:8px}
</style>
</head>
<body>
  <header class="site-header">
    <h1 class="site-title">VELVET COMPASS <span class="accent">DIARIES</span></h1>
    <nav class="main-nav">
      <a class="is-current" href="#">Home</a>
      <a href="#">About</a>
      <a href="#">Get the Book</a>
      <a href="#">Contact</a>
    </nav>
    <div class="nav-pointer"></div>
    <div class="nav-rule"></div>
  </header>

  <section class="book-cover">
    <div class="cover-card">
      <p class="cover-title">Velvet Compass Diaries</p>
      <p class="cover-tagline">Uncover hidden profit tricks insiders quietly bill huge sums over decades, hoping nobody ever finds out.</p>
    </div>
    <div class="cover-figure" role="img" aria-label="Silhouette of a businessman in a suit"></div>
    <p class="cover-author"><span class="by">by</span> Rowan Hale <span class="cred">CPA</span></p>
  </section>

  <div class="like-widget" aria-label="Chatterly like counter">
    <div class="like-count">0</div>
    <div class="like-brand"><span class="square"></span>Chatterly</div>
  </div>

  <svg class="guarantee-badge" viewBox="0 0 86 86" role="img" aria-label="100% money back guarantee seal">
    <circle cx="43" cy="43" r="42" fill="#cfcfcf"/>
    <circle cx="43" cy="43" r="36" fill="#00aaea"/>
    <circle cx="43" cy="43" r="29" fill="#fff"/>
    <circle cx="43" cy="43" r="26" fill="#111"/>
  </svg>

  <div class="pay-brand"><span class="dot"></span>Quidora</div>

  <section class="promo"></section>
  <div class="promo-rule"></div>
  <div class="promo-pointer"></div>
  <h2 class="promo-heading">PROMOTION</h2>

  <div class="video-shadow"></div>
  <div class="video-player" aria-label="ClipVaro promotional video">
    <svg class="spinner" width="18" height="18" viewBox="0 0 18 18">
      <g fill="#888">
        <circle cx="9" cy="2" r="1.6"/><circle cx="14" cy="4" r="1.6" opacity=".8"/>
        <circle cx="16" cy="9" r="1.6" opacity=".7"/><circle cx="14" cy="14" r="1.6" opacity=".6"/>
        <circle cx="9" cy="16" r="1.6" opacity=".5"/><circle cx="4" cy="14" r="1.6" opacity=".4"/>
        <circle cx="2" cy="9" r="1.6" opacity=".3"/><circle cx="4" cy="4" r="1.6" opacity=".2"/>
      </g>
    </svg>
    <div class="video-progress"></div>
    <div class="video-controls">
      <svg width="8" height="9" viewBox="0 0 8 9"><rect x="0" y="0" width="2.5" height="9" fill="#333"/><rect x="5" y="0" width="2.5" height="9" fill="#333"/></svg>
      <svg width="11" height="9" viewBox="0 0 11 9"><path d="M0 3h2l3-3v9L2 6H0z" fill="#333"/><path d="M7 2.5q2 2 0 4M8.5 1q3.5 3.5 0 7" stroke="#333" fill="none"/></svg>
      <span class="time">0:00 / 3:04</span>
      <span>360p</span>
      <svg width="10" height="8" viewBox="0 0 10 8"><rect x=".5" y=".5" width="9" height="7" fill="none" stroke="#333"/></svg>
      <svg width="10" height="8" viewBox="0 0 10 8"><path d="M1 2h7M6 0l2 2-2 2M9 6H2M4 4L2 6l2 2" stroke="#333" fill="none"/></svg>
      <svg width="9" height="9" viewBox="0 0 9 9"><path d="M0 3V0h3M6 0h3v3M9 6v3H6M3 9H0V6" stroke="#333" fill="none"/></svg>
    </div>
  </div>

  <footer class="site-footer">
    <span class="copyright">Copyright © 2013 Velvet Compass Diaries</span>
    <span class="legal">Privacy Policy &nbsp;&nbsp;|&nbsp;&nbsp; Terms and Conditions</span>
  </footer>
</body>
</html>
```